Lantern Quillhouse Website

Create website for Legal Management Company which specializes in Law Office Spersriinal Management
System implementation & Training
Global presence
Paralegal Services - Remote or In-Office
Legal Research
- Judge Motion Ruling History
- Opposing Counsel Opposition Research - Historical Filings - Pattern identification
Service by Mail - Ex- Parte Notice

Probate -Heir Finder - Asset Location -

```html
<!DOCTYPE html>
<html lang="en">
<head>
<meta charset="utf-8">
<title>Lantern Quillhouse — Strategic Legal Management</title>
<link rel="stylesheet" href="https://fonts.googleapis.com/css2?family=Inter:wght@400;500;600;700&family=Playfair+Display:ital,wght@0,400;0,500;0,600;1,400;1,500&display=swap">
<style>
:root{
  --navy:#0f1a2e;
  --navy-2:#16223a;
  --navy-line:#25324d;
  --accent:#e0801f;
  --ink:#0f1a2e;
  --muted:#4a5568;
  --soft:#f5f7fa;
  --line:#e5e9f0;
  --white:#fff;
  --serif:'Playfair Display', Georgia, serif;
  --sans:'Inter', Arial, sans-serif;
}
*{box-sizing:border-box;margin:0;padding:0}
html,body{width:1200px;height:4292px;overflow:hidden}
body{font-family:var(--sans);color:var(--ink);background:var(--white);position:relative}
.wrap{width:1084px;margin:0 auto;position:relative}
.eyebrow{font-size:11px;letter-spacing:2.4px;text-transform:uppercase;color:var(--accent);font-weight:600}
.serif{font-family:var(--serif)}

/* nav */
.nav{position:absolute;top:0;left:0;right:0;height:72px;z-index:3}
.nav .wrap{display:flex;align-items:center;justify-content:space-between;height:72px}
.brand{display:flex;align-items:center;gap:10px;font-family:var(--serif);font-weight:600;font-size:18px;color:var(--ink)}
.brand-mark{width:26px;height:26px;background:var(--navy);border-radius:3px}
.nav-links{display:flex;align-items:center;gap:28px;font-size:11px;letter-spacing:1.2px;color:#4a5568;font-weight:500}
.btn-dark{background:var(--navy);color:#fff;font-size:12px;font-weight:600;padding:10px 22px}

/* hero */
.hero{position:absolute;top:0;left:0;width:1200px;height:590px;background:linear-gradient(180deg,#fff 0%,#f7f9fc 100%);overflow:hidden}
.hero-photo{position:absolute;right:0;top:0;width:620px;height:590px;background:radial-gradient(ellipse at 70% 20%,#c9d6e2 0%,#e3eaf1 45%,rgba(255,255,255,0) 75%)}
.hero-text{position:absolute;left:58px;top:118px;width:520px}
.hero-tag{border-left:2px solid var(--accent);padding-left:10px;font-size:11px;letter-spacing:2px;color:#4a5568;font-weight:500}
.hero h1{font-family:var(--serif);font-weight:600;font-size:64px;line-height:70px;margin-top:22px;color:var(--ink)}
.hero h1 em{font-weight:400}
.hero p{font-size:16px;line-height:26px;color:var(--muted);margin-top:22px;width:450px}
.hero-ctas{display:flex;gap:14px;margin-top:30px}
.btn-outline{border:1px solid #cfd6e0;color:var(--ink);font-size:14px;padding:14px 28px;background:#fff}
.hero-ctas .btn-dark{font-size:14px;padding:14px 28px;display:flex;gap:8px;align-items:center}
.hero-card{position:absolute;left:685px;top:113px;width:393px;height:440px;background:rgba(255,255,255,.72);box-shadow:0 20px 50px rgba(15,26,46,.12)}
.hero-card .corner-tl{position:absolute;left:28px;top:28px;width:42px;height:42px;border-left:2px solid var(--accent);border-top:2px solid var(--accent)}
.hero-card .corner-br{position:absolute;right:28px;bottom:28px;width:42px;height:42px;border-right:2px solid var(--accent);border-bottom:2px solid var(--accent)}
.hero-card .num{position:absolute;right:30px;top:180px;font-family:var(--serif);font-size:46px;color:#e6ebf1;font-weight:600}
.hero-card .cap{position:absolute;right:30px;top:233px;text-align:right;font-size:11px;letter-spacing:1.6px;line-height:18px;color:#334}

/* about */
.about{position:absolute;top:590px;left:0;width:1200px;height:690px;background:#fff}
.center{text-align:center}
.about .eyebrow{margin-top:92px}
.about h2{font-family:var(--serif);font-weight:500;font-size:42px;line-height:53px;margin-top:18px}
.about h2 em{font-weight:400}
.about .lead{width:610px;margin:26px auto 0;font-size:15px;line-height:26px;color:var(--muted)}
.pillars{display:flex;gap:28px;margin-top:72px}
.pillar{flex:1;height:202px;border:1px solid var(--line);padding:34px 28px;background:#fff}
.pillar .ico{width:40px;height:40px;border-radius:50%;background:var(--soft);display:flex;align-items:center;justify-content:center}
.pillar h3{font-family:var(--serif);font-weight:500;font-size:17px;margin-top:20px}
.pillar p{font-size:12px;line-height:20px;color:var(--muted);margin-top:12px}

/* services */
.services{position:absolute;top:1280px;left:0;width:1200px;height:953px;background:var(--navy);color:#fff}
.services .eyebrow{margin-top:92px}
.services h2{font-family:var(--serif);font-weight:500;font-size:42px;line-height:43px;margin-top:16px;width:460px}
.services .desc{font-size:15px;line-height:25px;color:#a9b4c8;margin-top:24px;width:580px}
.btn-ghost{position:absolute;right:0;top:240px;border:1px solid #3a4763;font-size:12px;font-weight:500;padding:9px 15px}
.svc-grid{display:grid;grid-template-columns:repeat(3,347px);gap:21px 22px;margin-top:58px}
.svc{height:262px;border:1px solid var(--navy-line);background:var(--navy-2);border-radius:6px;padding:22px 22px 0;position:relative}
.svc .ico{width:40px;height:40px;border:1px solid #3a4763;border-radius:4px;display:flex;align-items:center;justify-content:center}
.svc h3{font-family:var(--serif);font-weight:500;font-size:17px;margin-top:24px}
.svc p{font-size:12px;line-height:20px;color:#98a4ba;margin-top:16px}
.svc .more{position:absolute;left:22px;right:22px;bottom:0;height:48px;border-top:1px solid var(--navy-line);display:flex;align-items:center;justify-content:space-between;font-size:10px;letter-spacing:1.2px;color:#6f7c95}

/* why */
.why{position:absolute;top:2233px;left:0;width:1200px;height:615px;background:var(--soft)}
.why-photo{position:absolute;left:58px;top:87px;width:514px;height:438px;background:linear-gradient(160deg,#e9e6df 0%,#cfc8bb 55%,#8f7a63 100%);box-shadow:0 18px 40px rgba(15,26,46,.15)}
.why-photo-edge{position:absolute;left:46px;top:87px;width:2px;height:80px;background:var(--accent)}
.quote{position:absolute;left:312px;top:432px;width:280px;height:115px;background:#fff;padding:30px 30px;font-family:var(--serif);font-style:italic;font-size:19px;line-height:25px;color:#222;box-shadow:0 10px 30px rgba(15,26,46,.1)}
.why-text{position:absolute;left:628px;top:82px;width:480px}
.why-text h2{font-family:var(--serif);font-weight:500;font-size:32px;line-height:40px;margin-top:16px}
.why-text .lead{font-size:15px;line-height:25px;color:var(--muted);margin-top:24px}
.checks{list-style:none;margin-top:28px}
.checks li{display:flex;align-items:center;gap:14px;font-size:13px;color:#2d3748;height:35px}

/* global */
.global{position:absolute;top:2848px;left:0;width:1200px;height:467px;background:#141d35;color:#fff}
.global .eyebrow{margin-top:90px}
.global h2{font-family:var(--serif);font-weight:500;font-size:43px;line-height:53px;margin-top:22px}
.global h2 em{color:var(--accent);font-weight:400}
.stats{display:flex;justify-content:center;gap:26px;margin-top:52px}
.stat{width:177px;height:100px;border:1px solid var(--navy-line);background:#19233d;text-align:center;padding-top:22px}
.stat b{display:block;font-size:27px;font-weight:600}
.stat span{display:block;font-size:11px;letter-spacing:1.3px;color:#8e9ab2;margin-top:8px}

/* contact */
.contact{position:absolute;top:3315px;left:0;width:1200px;height:685px;background:#fff}
.contact-card{position:absolute;left:150px;top:85px;width:898px;height:518px;display:flex;box-shadow:0 20px 50px rgba(15,26,46,.12)}
.contact-side{width:375px;background:var(--navy);color:#fff;padding:52px 42px;position:relative}
.contact-side h3{font-family:var(--serif);font-weight:500;font-size:26px}
.contact-side p{font-size:14px;line-height:23px;color:#a9b4c8;margin-top:20px}
.contact-side .k{font-size:10px;letter-spacing:1.6px;color:var(--accent);font-weight:600;margin-top:28px}
.contact-side .v{font-size:15px;margin-top:6px}
.contact-side .copy{position:absolute;left:42px;bottom:42px;font-size:10px;color:#6f7c95}
.form{flex:1;background:#fff;padding:38px 42px}
.row{display:flex;gap:22px}
.field{flex:1;margin-bottom:22px}
.field label{display:block;font-size:11px;font-weight:500;color:#2d3748;margin-bottom:6px}
.input{height:31px;border:1px solid #d7dce4;background:#f7f8fa;font-size:12px;color:#6b7280;padding:0 11px;display:flex;align-items:center}
.select{background:#fff;justify-content:space-between;color:#222}
.textarea{height:133px;align-items:flex-start;padding-top:11px}
.submit{height:42px;background:var(--navy);color:#fff;display:flex;align-items:center;justify-content:center;font-size:13px;font-weight:600;margin-top:-2px}

/* footer */
.footer{position:absolute;top:4000px;left:0;width:1200px;height:292px;background:#fff;border-top:1px solid var(--line)}
.footer-cols{display:flex;margin-top:38px}
.footer-brand{width:278px}
.footer-brand p{font-size:12px;line-height:19px;color:#5a6b85;margin-top:16px}
.fcol{width:278px}
.fcol h4{font-size:10px;letter-spacing:1.4px;font-weight:600;color:#2d3748;margin-top:8px}
.fcol a{display:block;font-size:12px;color:#4a5568;margin-top:12px;text-decoration:none}
.footer-bottom{position:absolute;left:58px;right:58px;top:238px;display:flex;justify-content:space-between;font-size:10px;color:#7a879c}
</style>
</head>
<body>

<section class="hero">
  <div class="hero-photo" role="img" aria-label="Soft, blurred photo of modern architectural facade in pale blue-grey light"></div>
  <div class="hero-text">
    <div class="hero-tag">GLOBAL LEGAL MANAGEMENT</div>
    <h1>Strategic Legal Management.<br><em>Research-Driven.</em></h1>
    <p>Global legal operations, paralegal services, and advanced legal research — delivered with precision for modern law firms and corporate departments.</p>
    <div class="hero-ctas">
      <span class="btn-dark">Request Consultation
        <svg width="12" height="12" viewBox="0 0 12 12" fill="none" stroke="#fff" stroke-width="1.5"><path d="M2 6h8M7 3l3 3-3 3"/></svg></span>
      <span class="btn-outline">Explore Services</span>
    </div>
  </div>
  <div class="hero-card">
    <div class="corner-tl"></div>
    <div class="num">01</div>
    <div class="cap">PRUDENCE &amp;<br>PRECISION</div>
    <div class="corner-br"></div>
  </div>
</section>

<header class="nav">
  <div class="wrap">
    <div class="brand"><span class="brand-mark"></span>Lantern Quillhouse</div>
    <nav class="nav-links">
      <span>ABOUT</span><span>SERVICES</span><span>WHY US</span><span>GLOBAL REACH</span>
      <span class="btn-dark">Consultation</span>
    </nav>
  </div>
</header>

<section class="about">
  <div class="wrap center">
    <div class="eyebrow">About Lantern Quillhouse</div>
    <h2>Elevating legal practice through<br><em>strategic management</em> &amp; insights.</h2>
    <p class="lead">We empower law firms, attorneys, and corporate legal departments with high-precision research and operational support. Our mission is to handle the complexities of legal management so you can focus on advocacy and strategy.</p>
    <div class="pillars" style="text-align:left">
      <div class="pillar">
        <div class="ico"><svg width="18" height="18" viewBox="0 0 24 24" fill="none" stroke="#0f1a2e" stroke-width="1.7"><circle cx="12" cy="12" r="9"/><path d="M3 12h18M12 3c3 3 3 15 0 18M12 3c-3 3-3 15 0 18"/></svg></div>
        <h3>Global Presence</h3>
        <p>Seamless legal operations across international jurisdictions with localized expertise.</p>
      </div>
      <div class="pillar">
        <div class="ico"><svg width="18" height="18" viewBox="0 0 24 24" fill="none" stroke="#0f1a2e" stroke-width="1.7"><path d="M3 5h6a3 3 0 013 3v12a2 2 0 00-2-2H3zM21 5h-6a3 3 0 00-3 3v12a2 2 0 012-2h7z"/></svg></div>
        <h3>Legal Expertise</h3>
        <p>Deep knowledge in probate, litigation support, and regulatory compliance.</p>
      </div>
      <div class="pillar">
        <div class="ico"><svg width="18" height="18" viewBox="0 0 24 24" fill="none" stroke="#0f1a2e" stroke-width="1.7"><path d="M12 3l8 3v6c0 5-4 8-8 9-4-1-8-4-8-9V6z"/><path d="M9 12l2 2 4-4"/></svg></div>
        <h3>Operational Excellence</h3>
        <p>Streamlined workflows and strict confidentiality protocols for sensitive matters.</p>
      </div>
    </div>
  </div>
</section>

<section class="services">
  <div class="wrap">
    <div class="eyebrow">Our Expertise</div>
    <h2>Comprehensive Legal Solutions</h2>
    <p class="desc">Tailored services designed to enhance efficiency and provide a competitive edge in legal proceedings.</p>
    <span class="btn-ghost">Discuss Requirements</span>
    <div class="svc-grid">
      <div class="svc">
        <div class="ico"><svg width="16" height="16" viewBox="0 0 24 24" fill="none" stroke="#e0801f" stroke-width="1.7"><rect x="4" y="4" width="16" height="17"/><path d="M8 8h2M14 8h2M8 12h2M14 12h2M8 16h2M14 16h2"/></svg></div>
        <h3>Law Office Management</h3>
        <p>Comprehensive operational management, system implementation, training, and workflow optimization for modern firms.</p>
        <div class="more">LEARN MORE<span>↗</span></div>
      </div>
      <div class="svc">
        <div class="ico"><svg width="16" height="16" viewBox="0 0 24 24" fill="none" stroke="#e0801f" stroke-width="1.7"><rect x="3" y="7" width="18" height="13" rx="1"/><path d="M9 7V4h6v3M12 7v13"/></svg></div>
        <h3>Paralegal Services</h3>
        <p>Flexible remote or in-office support providing confidential, compliant, and expert assistance for case management.</p>
        <div class="more">LEARN MORE<span>↗</span></div>
      </div>
      <div class="svc">
        <div class="ico"><svg width="16" height="16" viewBox="0 0 24 24" fill="none" stroke="#e0801f" stroke-width="1.7"><circle cx="11" cy="11" r="6"/><path d="M16 16l4 4"/></svg></div>
        <h3>Legal Research</h3>
        <p>In-depth analysis of judge motion rulings, opposing counsel research, historical filings review, and pattern identification.</p>
        <div class="more">LEARN MORE<span>↗</span></div>
      </div>
      <div class="svc">
        <div class="ico"><svg width="16" height="16" viewBox="0 0 24 24" fill="none" stroke="#e0801f" stroke-width="1.7"><rect x="3" y="5" width="18" height="14" rx="1"/><path d="M3 6l9 7 9-7"/></svg></div>
        <h3>Legal Process Support</h3>
        <p>Precision execution of service by mail, ex-parte notice handling, and compliance-focused delivery tracking.</p>
        <div class="more">LEARN MORE<span>↗</span></div>
      </div>
      <div class="svc">
        <div class="ico"><svg width="16" height="16" viewBox="0 0 24 24" fill="none" stroke="#e0801f" stroke-width="1.7"><path d="M6 3h10v14a3 3 0 01-3 3H7a3 3 0 01-3-3v-2h9"/><path d="M9 7h4M9 11h4"/></svg></div>
        <h3>Probate Services</h3>
        <p>Specialized heir finding, asset location, and comprehensive probate research support for estate matters.</p>
        <div class="more">LEARN MORE<span>↗</span></div>
      </div>
    </div>
  </div>
</section>

<section class="why">
  <div class="why-photo-edge"></div>
  <div class="why-photo" role="img" aria-label="Photo of a quiet private office with a wooden desk, chair and bookshelf"></div>
  <div class="quote">"Precision is not an act,<br>it is a habit."</div>
  <div class="why-text">
    <div class="eyebrow">Why Choose Lantern Quillhouse</div>
    <h2>A strategic partner for<br>complex legal challenges.</h2>
    <p class="lead">We move beyond traditional support. Our approach combines rigorous research methodologies with modern operational efficiency, ensuring that every detail is accounted for.</p>
    <ul class="checks">
      <li><svg width="18" height="18" viewBox="0 0 20 20" fill="none" stroke="#e0801f" stroke-width="1.6"><circle cx="10" cy="10" r="8"/><path d="M6.5 10l2.5 2.5 4.5-5"/></svg>Data-driven legal research methodologies</li>
      <li><svg width="18" height="18" viewBox="0 0 20 20" fill="none" stroke="#e0801f" stroke-width="1.6"><circle cx="10" cy="10" r="8"/><path d="M6.5 10l2.5 2.5 4.5-5"/></svg>Confidential &amp; compliant workflow systems</li>
      <li><svg width="18" height="18" viewBox="0 0 20 20" fill="none" stroke="#e0801f" stroke-width="1.6"><circle cx="10" cy="10" r="8"/><path d="M6.5 10l2.5 2.5 4.5-5"/></svg>Global legal support capabilities</li>
      <li><svg width="18" height="18" viewBox="0 0 20 20" fill="none" stroke="#e0801f" stroke-width="1.6"><circle cx="10" cy="10" r="8"/><path d="M6.5 10l2.5 2.5 4.5-5"/></svg>Precision-focused legal operations</li>
      <li><svg width="18" height="18" viewBox="0 0 20 20" fill="none" stroke="#e0801f" stroke-width="1.6"><circle cx="10" cy="10" r="8"/><path d="M6.5 10l2.5 2.5 4.5-5"/></svg>Trusted by senior legal professionals</li>
      <li><svg width="18" height="18" viewBox="0 0 20 20" fill="none" stroke="#e0801f" stroke-width="1.6"><circle cx="10" cy="10" r="8"/><path d="M6.5 10l2.5 2.5 4.5-5"/></svg>Rapid response and turnaround times</li>
    </ul>
  </div>
</section>

<section class="global">
  <div class="wrap center">
    <div class="eyebrow">Global Capabilities</div>
    <h2>Serving legal professionals across<br>borders with <em>localized expertise.</em></h2>
    <div class="stats">
      <div class="stat"><b>24/7</b><span>SUPPORT</span></div>
      <div class="stat"><b>50+</b><span>JURISDICTIONS</span></div>
      <div class="stat"><b>100%</b><span>COMPLIANCE</span></div>
      <div class="stat"><b>10+</b><span>YEARS EXP.</span></div>
    </div>
  </div>
</section>

<section class="contact">
  <div class="contact-card">
    <div class="contact-side">
      <h3>Start a Conversation</h3>
      <p>Schedule a confidential consultation to discuss your firm's specific needs. We prioritize discretion and efficiency.</p>
      <div class="k">EMAIL</div>
      <div class="v">hello@lanternquillhouse.example</div>
      <div class="k">OFFICE</div>
      <div class="v">London • New York • Singapore</div>
      <div class="copy">© 2024 Lantern Quillhouse. All rights reserved.</div>
    </div>
    <div class="form">
      <div class="row">
        <div class="field"><label>Name</label><div class="input">John Doe</div></div>
        <div class="field"><label>Email Address</label><div class="input">john@lawfirm.com</div></div>
      </div>
      <div class="field"><label>Company / Law Firm</label><div class="input">Smith &amp; Associates</div></div>
      <div class="field"><label>Service of Interest</label><div class="input select">Select a service...<svg width="10" height="10" viewBox="0 0 10 10" fill="none" stroke="#222" stroke-width="1.5"><path d="M2 4l3 3 3-3"/></svg></div></div>
      <div class="field"><label>Message</label><div class="input textarea">How can we assist you?</div></div>
      <div class="submit">Schedule Confidential Consultation</div>
    </div>
  </div>
</section>

<footer class="footer">
  <div class="wrap">
    <div class="footer-cols">
      <div class="footer-brand">
        <div class="brand"><span class="brand-mark"></span>Lantern Quillhouse</div>
        <p>Strategic Legal Management.<br>Research-Driven Results.</p>
      </div>
      <div class="fcol"><h4>SERVICES</h4><a>Law Office Management</a><a>Paralegal Services</a><a>Legal Research</a><a>Probate Support</a></div>
      <div class="fcol"><h4>COMPANY</h4><a>About Us</a><a>Why Choose Us</a><a>Contact</a><a>Careers</a></div>
      <div class="fcol" style="width:auto"><h4>LEGAL</h4><a>Privacy Policy</a><a>Terms of Service</a><a>Disclaimer</a></div>
    </div>
  </div>
  <div class="footer-bottom"><span>© 2025 Lantern Quillhouse. All rights reserved.</span><span>Designed with precision.</span></div>
</footer>

</body>
</html>
```